Secret agents need a new website

We organize child birthdays with a special agents in london & Bristol.

Current design does not grab people attention, and they leave website too soon.

Colors. Up to 3 main colors, but maybe black + green + white, or blact + red + white, would suit our secret operations website.

Current website:
www.moonjumble.co.uk

Dear designers, thanks very much for working on our design.

Please try to make like a SPECIAL YOUNG AGENT TRAINING WEBSITE, all other
entertainers have childish websites, and we want to differentiate from them.

Not sure if it helps, but I like this design very much:

Guys,

I am looking for spy/secret agent/action themed design. You submitting awesome designs, and if I have another business, I just choose any of them at it would be perfect. But I want spy/secret agent/action themed.

Please feel free to add elements like:

1. Yellow, or RED line CRIME SCENE DO NOT CROSS
2. Some words or phrases can be black background - white text. 
3. Some stamps like this:
http://www.plenvoria.com/pic-48120957/stock-vector-assorted-office-ink-marks-classified-private-etc.html?src=qTm4Lo-bRwNxZ3e-p81KcE-1-16

4.spy guys http://www.plenvoria.com/pic-39418275/stock-vector-sleuth-in-long-overcoat-vintage-clip-art.html?src=hdWpRmTeQoXs4v9bnaLjCf-1-9

Do not make too much elements, I like simple designs, less details.  

PLEASE NO CHILDS WITH GUNS, and better NO GUNS at all. 

Target Market(s)

Audience: Woman, but should look cool for kids too.
(Please DO NOT make design childish)

Requirements
Must have
• Please take a look at current website
• 1. Texts should be easy to read and not too small.
• 2. White/bright background
• 3. Lead form should stay on page
• 4. Header, and footer should be not too big.
• 5. Infographic is not needed
• Extra elements
• 1. Company blog
• 2. Client zone
• 3. Venue finder
• 4. How to pay deposit
Nice to have
• We accept
• Quidlo
• marrowfeld
• (please browse logos)
• On header would be better to use
• MoonJumble.co.uk
• But also add somethere, in association with Fen-rally.co.uk.
• Please use logo with .co.uk
• In archive you will find without background if needed too.

```html
<!DOCTYPE html>
<html lang="en">
<head>
<meta charset="utf-8">
<title>Fen-rally.co.uk – Top Secret Spy Party</title>
<link href="https://fonts.googleapis.com/css2?family=Raleway:wght@300;400;600;700;800&family=Open+Sans:wght@400;600;700&display=swap" rel="stylesheet">
<style>
:root{
  --green:#8cc63e;
  --ink:#1b1b1b;
  --charcoal:#2e2e2e;
  --red:#d52b2b;
  --grey:#777;
  --light:#eeeeee;
  --white:#ffffff;
}
*{box-sizing:border-box;margin:0;padding:0}
html,body{width:1200px;height:2972px;overflow:hidden}
body{position:relative;background:var(--white);font-family:"Open Sans",Arial,sans-serif;color:var(--grey)}
.abs{position:absolute}

/* header */
.site-header{left:0;top:0;width:1200px;height:400px;background:var(--white)}
.brand{left:0;width:1200px;top:170px;text-align:center}
.brand-name{display:inline-flex;align-items:center;gap:18px;font-family:"Open Sans",sans-serif;font-weight:600;font-size:44px;color:var(--ink)}
.brand-mark{width:40px;height:40px;background:var(--ink)}

/* nav */
.main-nav{left:0;top:400px;width:1200px;height:60px;background:var(--ink);display:flex;align-items:center;padding:0 80px}
.main-nav a{font-family:"Raleway",sans-serif;font-weight:700;font-size:17px;color:var(--white);text-decoration:none;margin-right:56px}
.social{margin-left:auto;display:flex;gap:24px}
.social span{width:16px;height:16px;background:#bbb;display:block}

/* hero */
.hero{left:0;top:460px;width:1200px;height:480px;background:linear-gradient(180deg,#3d3d3d,#262626)}
.hero-copy{left:80px;top:56px;width:480px;color:var(--white)}
.hero-quote{font-family:"Raleway",sans-serif;font-weight:300;font-size:33px;line-height:1.28}
.hero-title{font-family:"Raleway",sans-serif;font-weight:700;font-size:42px;color:var(--green);line-height:1.15;margin-top:6px}
.hero-sub{font-family:"Raleway",sans-serif;font-weight:300;font-size:24px;line-height:1.35;margin-top:36px}
.hero-sub b{font-weight:700}
.video{left:620px;top:52px;width:520px;height:388px}

/* about */
.photo-stack{left:80px;top:980px;width:400px;height:340px;background:linear-gradient(135deg,#e6e6e6,#9a9a9a)}
.about-copy{left:580px;top:990px;width:580px;font-size:15.5px;line-height:1.55}
.about-copy p{margin-bottom:18px}
.tag{background:var(--ink);color:var(--white);font-weight:700;padding:1px 6px;font-size:14px}

/* dark info band */
.info{left:0;top:1500px;width:1200px;height:780px;background:var(--charcoal)}
.ribbon{left:60px;top:1348px;width:190px;height:44px;background:var(--red);color:var(--white);font-family:"Raleway",sans-serif;font-weight:700;font-size:20px;display:flex;align-items:center;justify-content:center;transform:rotate(-6deg);z-index:3}
.id-card{left:100px;top:1380px;width:500px;height:290px;background:linear-gradient(135deg,#f2f2f2,#8a8a8a);z-index:2}
.col{width:280px;font-size:14px;line-height:1.55;color:#cfcfcf}
.col h3{font-family:"Raleway",sans-serif;font-weight:600;font-size:22px;line-height:1.25;color:var(--green);margin-bottom:12px}
.col p{margin-bottom:22px}
.col b{color:var(--white)}
.col-1{left:80px;top:1700px}
.col-2{left:440px;top:1700px}
.col-3{left:820px;top:1590px;width:320px}

/* quote form */
.skyline{left:0;top:2460px;width:1200px;height:420px;background:linear-gradient(180deg,#ffffff,#e2e2e2)}
.quote-title{left:80px;top:2320px;font-family:"Raleway",sans-serif;font-weight:700;font-size:34px;color:var(--green)}
.field-label{font-size:17px;color:#555}
.field{height:36px;background:var(--light);border:1px solid #ddd}
.respond{left:790px;top:2500px;width:170px;font-size:15px;line-height:1.35;color:#555}
.enquiry{left:970px;top:2500px;width:150px;height:46px;background:var(--ink);color:var(--white);font-family:"Raleway",sans-serif;font-weight:800;font-size:20px;display:flex;align-items:center;justify-content:center}
.call{left:80px;top:2580px;width:440px;height:64px;background:var(--red);color:var(--white);font-family:"Raleway",sans-serif;font-size:24px;display:flex;align-items:center;justify-content:center;gap:14px}
.call b{font-weight:800;font-size:28px}

/* footer */
.site-footer{left:0;top:2880px;width:1200px;height:92px;background:#d8d8d8;text-align:center;padding-top:14px}
.footer-links{display:flex;justify-content:center;gap:10px}
.footer-links a{background:var(--ink);color:var(--white);font-family:"Raleway",sans-serif;font-weight:700;font-size:15px;padding:5px 14px;text-decoration:none}
.copyright{font-size:13px;color:#555;margin-top:12px}
</style>
</head>
<body>

<header class="site-header abs">
  <div class="brand abs">
    <div class="brand-name"><span class="brand-mark"></span>Fen-rally.co.uk</div>
  </div>
</header>

<nav class="main-nav abs">
  <a href="#">HOME</a><a href="#">EQUIPMENT</a><a href="#">INVITATIONS</a><a href="#">PARTY</a><a href="#">BAGSPRICES</a>
  <div class="social"><span></span><span></span></div>
</nav>

<section class="hero abs">
  <div class="hero-copy abs">
    <p class="hero-quote">I wanted a kids birthday party with a difference, and then I found the</p>
    <p class="hero-title">Top Secret Spy Party</p>
    <p class="hero-sub">Capture your kids imagination with a <b>Spy Birthday Party</b> in London, Bristol</p>
  </div>
  <svg class="video abs" viewBox="0 0 520 388" role="img" aria-label="Video player">
    <rect width="520" height="388" fill="#0d0d0d"/>
    <polygon points="238,160 238,220 288,190" fill="#ffffff" opacity=".85"/>
    <rect x="0" y="358" width="520" height="30" fill="#1f1f1f"/>
    <rect x="60" y="371" width="400" height="4" fill="#555"/>
  </svg>
</section>

<section class="about">
  <div class="photo-stack abs" role="img" aria-label="Stacked instant photos of young party agents"></div>
  <div class="about-copy abs">
    <p>Every parent wants to give their child the best birthday party, but we don't always have the time to plan and prepare for an extra special birthday party with the wow factor.</p>
    <p>We created this Spy party to be fun from beginning to end. Your child will send their guests cool <span class="tag">TOP SECRET INVITATIONS</span> to a party where they will take part in Secret Agent Training. The children will be so excited that they won't be able to stop talking about it.</p>
    <p>At the party all the children will become special agents, trying out <span class="tag">SPY GEAR</span> and finding out how to be a great spy in our fun secret agent games. It's a great way to get the children interested in new things, working together in teams and using their imagination. Every child that takes part will receive a Spy School Secret Agent certificate and your <span class="tag">SPY PARTY BAG</span> to take away and continue the fun with their friends at home and at school.</p>
  </div>
</section>

<section class="info abs"></section>
<div class="ribbon abs">Spy ID example</div>
<div class="id-card abs" role="img" aria-label="Example spy school ID card with agent photo"></div>

<div class="col col-1 abs">
  <h3>How many children can come to a Spy Birthday Party?</h3>
  <p>We provide parties for groups of up to 30 children. For groups of up to 12 we will provide one <b>ENTERTAINER</b>, for larger groups we will provide more <b>ENTERTAINERS</b> to ensure all the children get a great experience.</p>
  <h3>How old should the children be?</h3>
  <p>The Spy Birthday party is aimed at children aged 6 to 12, but we can adapt it for younger ones too.</p>
</div>

<div class="col col-2 abs">
  <h3>Where can we have a Spy Birthday Party?</h3>
  <p>You can have a Spy Birthday Party anywhere: at your home, at a cafe or a church hall. If you need help finding a venue let us know and we can help find a great place.</p>
  <h3>How much does it cost?</h3>
  <p>The cost depends on how many children will be taking part. For groups up to 12 with one entertainer running the party, it costs £129.99. For larger groups have a look at our <b>PRICES</b>.</p>
  <h3>Who are our ENTERTAINERS?</h3>
  <p>All our <b>ENTERTAINERS</b> are CRB checked and are fully trained to organise this type of birthday. After every party we ask our clients for</p>
</div>

<div class="col col-3 abs">
  <p>feedback on the event, which helps our entertainers to continually evaluate and improve their performance.</p>
  <h3>Is this a great party?</h3>
  <p>Many of our bookings come through recommendation. We have previous clients that would be happy to share their experience of a Spy Birthday Party. If you would like to talk to them let us know. You can also see some of our <b>CLIENT FEEDBACK</b>.</p>
  <p>Wed like to help you organise a party your child will remember. We appreciate that people have busy lives and organising a party can be hard work – so let us make it easy for you!</p>
  <p>Please fill in your information below, or call us and we can check our availability on your chosen date.</p>
</div>

<div class="skyline abs" role="img" aria-label="Faint city skyline silhouette"></div>
<h2 class="quote-title abs">Request a quote now!</h2>

<span class="field-label abs" style="left:80px;top:2400px">Your name</span>
<div class="field abs" style="left:230px;top:2394px;width:330px"></div>
<span class="field-label abs" style="left:80px;top:2460px">Your e-mail</span>
<div class="field abs" style="left:230px;top:2454px;width:330px"></div>
<span class="field-label abs" style="left:80px;top:2520px">Your city</span>
<div class="field abs" style="left:230px;top:2514px;width:330px"></div>

<span class="field-label abs" style="left:660px;top:2400px">Your phone</span>
<div class="field abs" style="left:790px;top:2394px;width:330px"></div>
<span class="field-label abs" style="left:660px;top:2460px">7 + 3 =</span>
<div class="field abs" style="left:790px;top:2454px;width:330px"></div>
<p class="respond abs">We will respond within 24 hours Monday – Friday</p>
<div class="enquiry abs">ENQUIRY</div>

<div class="call abs">Or just give us a call <b>3610 4475</b></div>

<footer class="site-footer abs">
  <div class="footer-links"><a href="#">CONTACT US</a><a href="#">ABOUT US</a><a href="#">TERMS AND CONDITIONS</a></div>
  <p class="copyright">Copyright © 2010-2013 Brightwell Events Ltd</p>
</footer>

</body>
</html>
```